Veranaxis Business Card and Letter Head

We are a leadership assessment consultancy based in Sydney, Australia. We help executive-level decison-makers select leaders for more senior level roles in corporate and government organisations. Our methodology is based on the latest research from the field of neuroscience.
We need a business card design and matching letter head that presents our company, Veranaxis, as a:
1. trusted adviser to senior executive-level decison makers
2. niche consultancy who are experts in the field of assessing leadership talent
3. results-focused solution provider who balance scientific methods with pragmatic solutions
The following company details should be used in all designs:
Company Name: Veranaxis
Details (for business card):
Daniel Prescott
Senior Talent Advisor
Level 17, Brenning Tower
7 Brenning Square
Carrowby, NSW 2417 Australia
Phone: 1300 482 716
Mobile: 0412 573 208
Email: daniel.prescott@veranaxis.com.au
Website: veranaxis.com.au
I have attached the logo for Veranaxis (for both a white and black background) - your business card and letter head designs must incoporate this logo and colour scheme.
Thanks for your interest in this project, I'm looking forward to receiving your ideas.
Regards,
Daniel
Executive-level decison-makers in corporate and government organisations (e.g., CEO, VP, Head of Human Resources)
Leadership

```html
<!DOCTYPE html>
<html lang="en">
<head>
<meta charset="utf-8">
<title>Veranaxis Business Card</title>
<link rel="stylesheet" href="https://fonts.googleapis.com/css2?family=Open+Sans:wght@400;600;700;800&display=swap">
<style>
  :root {
    --red: #c1272d;
    --charcoal: #3e3e40;
    --grey: #6b6b6d;
    --rule: #c9c9c9;
    --paper: #ffffff;
    --backdrop: #e8e6e3;
  }
  * { margin: 0; padding: 0; box-sizing: border-box; }
  html, body { width: 1200px; height: 1094px; overflow: hidden; }
  body {
    background: var(--backdrop);
    font-family: "Open Sans", Arial, sans-serif;
    color: var(--charcoal);
    position: relative;
  }
  .card {
    position: absolute;
    left: 180px;
    width: 840px;
    height: 480px;
    background: var(--paper);
    border-radius: 30px;
    overflow: hidden;
    box-shadow: 0 6px 20px rgba(0,0,0,0.12);
  }
  .card--front { top: 40px; }
  .card--back { top: 574px; }

  .brand { position: absolute; display: flex; flex-direction: column; white-space: nowrap; }
  .brand__row { display: flex; align-items: center; gap: 22px; }
  .brand__mark { width: 34px; height: 34px; background: var(--red); flex: none; }
  .brand__name { font-weight: 800; font-size: 92px; line-height: 1; letter-spacing: -2px; color: var(--charcoal); }
  .brand__tagline { font-size: 25px; letter-spacing: 2px; color: var(--grey); text-transform: uppercase; margin-top: 6px; padding-left: 56px; }
  .card--front .brand { left: 70px; top: 50px; }
  .card--back .brand { left: 50%; top: 50%; transform: translate(-50%, -50%); }

  .person { position: absolute; left: 150px; top: 232px; white-space: nowrap; }
  .person__name { font-weight: 700; font-size: 30px; color: var(--red); }
  .person__title { font-size: 19px; font-weight: 600; color: var(--charcoal); }
  .address { position: absolute; left: 80px; top: 282px; font-size: 19px; color: var(--charcoal); white-space: nowrap; }

  .contacts { position: absolute; left: 250px; top: 326px; display: flex; gap: 22px; font-size: 18px; white-space: nowrap; }
  .contacts__col { display: flex; flex-direction: column; gap: 4px; }
  .contacts__col + .contacts__col { border-left: 2px solid var(--rule); padding-left: 20px; }
  .contact { display: flex; align-items: center; gap: 9px; }
  .contact svg { width: 17px; height: 17px; fill: var(--red); flex: none; }

  .bands { position: absolute; left: 0; bottom: 0; width: 840px; height: 80px; }
  .bands__url { position: absolute; right: 60px; bottom: 16px; color: #fff; font-size: 27px; font-weight: 600; }
</style>
</head>
<body>
  <section class="card card--front">
    <div class="brand">
      <div class="brand__row">
        <span class="brand__mark"></span>
        <span class="brand__name">Veranaxis</span>
      </div>
      <span class="brand__tagline">Assessing Executive Capacity</span>
    </div>

    <p class="person"><span class="person__name">Daniel Prescott,</span> <span class="person__title">Senior Talent Advisor</span></p>
    <p class="address">Level 17, Brenning Tower 7 Brenning Square Carrowby, NSW 2417 Australia</p>

    <div class="contacts">
      <div class="contacts__col">
        <span class="contact">
          <svg viewBox="0 0 24 24"><path d="M6.6 10.8a15.1 15.1 0 0 0 6.6 6.6l2.2-2.2a1 1 0 0 1 1-.25 11.4 11.4 0 0 0 3.6.57 1 1 0 0 1 1 1V20a1 1 0 0 1-1 1A17 17 0 0 1 3 4a1 1 0 0 1 1-1h3.5a1 1 0 0 1 1 1c0 1.25.2 2.45.57 3.57a1 1 0 0 1-.25 1z"/></svg>
          1300 482 716
        </span>
        <span class="contact">
          <svg viewBox="0 0 24 24"><path d="M7 1h10a2 2 0 0 1 2 2v18a2 2 0 0 1-2 2H7a2 2 0 0 1-2-2V3a2 2 0 0 1 2-2zm0 4v13h10V5zm5 14.5a1.2 1.2 0 1 0 0 2.4 1.2 1.2 0 0 0 0-2.4z"/></svg>
          0412 573 208
        </span>
      </div>
      <div class="contacts__col">
        <span class="contact">
          <svg viewBox="0 0 24 24"><path d="M2 5h20v14H2zm2 2v.4l8 5 8-5V7zm0 2.8V17h16V9.8l-8 5z"/></svg>
          daniel.prescott@veranaxis.com.au
        </span>
        <span class="contact">
          <svg viewBox="0 0 24 24"><path d="M12 2a10 10 0 1 0 0 20 10 10 0 0 0 0-20zm6.9 6h-3a15 15 0 0 0-1.3-3.9A8 8 0 0 1 18.9 8zM12 4c.8 1.2 1.5 2.5 1.9 4h-3.8c.4-1.5 1.1-2.8 1.9-4zM4.3 14a8 8 0 0 1 0-4h3.4a16 16 0 0 0 0 4zm.8 2h3a15 15 0 0 0 1.3 3.9A8 8 0 0 1 5.1 16zm3-8h-3a8 8 0 0 1 4.3-3.9A15 15 0 0 0 8.1 8zM12 20c-.8-1.2-1.5-2.5-1.9-4h3.8c-.4 1.5-1.1 2.8-1.9 4zm2.3-6H9.7a14 14 0 0 1 0-4h4.6a14 14 0 0 1 0 4zm.3 5.9a15 15 0 0 0 1.3-3.9h3a8 8 0 0 1-4.3 3.9zm1.7-5.9a16 16 0 0 0 0-4h3.4a8 8 0 0 1 0 4z"/></svg>
          www.veranaxis.com.au
        </span>
      </div>
    </div>

    <div class="bands">
      <svg width="840" height="80" viewBox="0 0 840 80">
        <polygon points="0,32 330,32 306,80 0,80" fill="var(--charcoal)"/>
        <polygon points="352,0 840,0 840,80 312,80" fill="var(--red)"/>
      </svg>
      <span class="bands__url">www.veranaxis.com.au</span>
    </div>
  </section>

  <section class="card card--back">
    <div class="brand">
      <div class="brand__row">
        <span class="brand__mark"></span>
        <span class="brand__name">Veranaxis</span>
      </div>
      <span class="brand__tagline">Assessing Executive Capacity</span>
    </div>
  </section>
</body>
</html>
```